Brochure for people who suffer from Sleep Apnea and need a medical device called a CPAP Machine

I want a brochure that can be placed in doctors offices with my competitors brochures. It needs to be bold and stand out and deliver a very strong message that draws the patients away from our competitors and to us. I have included a word document generally outlining some of my requirements and thoughts, please review prior to investing time into design!

Target Market(s)

people who suffer from sleep apnea, which is a disease that causes them to stop breathing many times per hour, resulting in the patient needing to wear a device called a CPAP Machine. This is an illness that can impact anyone but is more likely to impact those suffering from obesity and men.

Industry/Entity Type

Health Care

Other font styles liked:
• Use what you think is best

Colors

Designer to choose colors to be used in the design.

Requirements
Must have
• Please see word document for must have items, and feel free to contact me with any questions.
• Also must have bold colors, and/or graphics to really stand out among my competitors brochures.
Nice to have
• Would prefer to use the baby picture titled "sleeping baby 4" if possible but provided 2 other baby photos just in case. Whatever you want to add, use your professional creativity! You Don't need to use all the pictures uploaded!!!!!
Should not have
• Nothing discriminatory or offensive.

```html
<!DOCTYPE html>
<html lang="en">
<head>
<meta charset="utf-8">
<title>RestWell Direct – Trifold Brochure</title>
<link href="https://fonts.googleapis.com/css2?family=Catamaran:wght@400;500;600;700&display=swap" rel="stylesheet">
<style>
  :root {
    --green: #1fa463;
    --purple: #8c4fb0;
    --ink: #1f1f1f;
    --paper: #ffffff;
    --stage: #e9e9ec;
    --seal-gold: #e8b425;
    --seal-red: #c62828;
  }
  * { margin: 0; padding: 0; box-sizing: border-box; }
  html, body { width: 1200px; height: 903px; overflow: hidden; background: var(--stage); }
  body { font-family: "Catamaran", sans-serif; color: var(--ink); }

  .brochure {
    position: absolute; left: 15px; top: 11px;
    width: 1170px; height: 880px;
    background: var(--paper);
    box-shadow: 0 2px 10px rgba(0,0,0,.15);
    overflow: hidden;
  }
  .brochure-art { position: absolute; inset: 0; }
  .abs { position: absolute; }

  /* Panel 1 – services */
  .intro { left: 27px; top: 22px; width: 337px; font-size: 13.5px; line-height: 1.3; font-weight: 600; color: var(--green); text-align: justify; }
  .lead { left: 27px; top: 86px; width: 337px; font-size: 13.5px; line-height: 1.3; font-weight: 600; }
  .service { left: 27px; width: 340px; display: flex; gap: 12px; }
  .service-icon { flex: 0 0 26px; height: 26px; }
  .service-title { font-size: 13.5px; font-weight: 600; color: var(--purple); line-height: 1.25; }
  .service-text { font-size: 13.5px; line-height: 1.3; }
  .settle { left: 27px; top: 544px; font-size: 18px; line-height: 1.2; font-weight: 500; color: var(--green); }
  .personal { left: 27px; top: 596px; font-size: 18px; font-weight: 500; color: var(--purple); }

  /* Panel 2 – contact */
  .warning { left: 411px; top: 22px; font-size: 15px; line-height: 1.3; font-weight: 600; color: var(--green); }
  .warning span { display: block; color: var(--purple); }
  .brand-name { font-weight: 400; color: var(--green); white-space: nowrap; letter-spacing: .2px; }
  .brand-mid { left: 390px; width: 300px; top: 384px; text-align: center; font-size: 31px; }
  .contact { left: 414px; width: 300px; display: flex; gap: 10px; font-size: 13.5px; line-height: 1.3; }
  .contact svg { flex: 0 0 18px; height: 18px; margin-top: 1px; }
  .promise { left: 411px; top: 608px; width: 260px; font-size: 14px; line-height: 1.2; font-weight: 600; }
  .tagline-mid { left: 390px; width: 300px; top: 842px; text-align: center; font-size: 21px; font-weight: 500; color: #fff; }

  /* Panel 3 – cover */
  .brand-cover { left: 780px; width: 390px; top: 92px; text-align: center; font-size: 38px; }
  .cover-head { left: 780px; width: 370px; text-align: center; }
  .want { top: 216px; font-size: 32px; font-weight: 700; color: var(--green); }
  .baby { top: 256px; font-size: 27px; font-weight: 500; }
  .show { top: 294px; font-size: 24px; font-weight: 700; color: var(--purple); }
  .diff { left: 780px; width: 390px; top: 684px; text-align: center; font-size: 19px; font-weight: 600; color: #fff; }
  .perks { left: 808px; top: 720px; width: 340px; display: grid; grid-template-columns: 128px 1fr; row-gap: 2px; font-size: 13px; font-weight: 500; color: #fff; }
  .perks li { list-style: none; position: relative; padding-left: 14px; }
  .perks li::before { content: ""; position: absolute; left: 0; top: 6px; width: 7px; height: 7px; border-radius: 50%; background: var(--green); }
  .blurb { left: 806px; top: 772px; width: 337px; font-size: 11.5px; line-height: 1.35; font-style: italic; color: #eadcf2; text-align: justify; }
  .tagline-cover { left: 780px; width: 390px; top: 818px; text-align: center; font-size: 15px; font-weight: 600; color: #fff; }
  .contact-pill {
    left: 806px; top: 845px; width: 338px; height: 28px;
    border: 1.5px solid #fff; border-radius: 14px; background: var(--green);
    display: flex; align-items: center; justify-content: center; gap: 18px;
    font-size: 13px; font-weight: 500; color: #fff;
  }
  .contact-pill span { display: flex; align-items: center; gap: 6px; }
</style>
</head>
<body>
<div class="brochure">
  <svg class="brochure-art" width="1170" height="880" viewBox="0 0 1170 880" xmlns="http://www.w3.org/2000/svg">
    <defs>
      <linearGradient id="toneCouple" x1="0" y1="0" x2="1" y2="1">
        <stop offset="0" stop-color="#f4f2f1"/>
        <stop offset=".5" stop-color="#e7d6cb"/>
        <stop offset="1" stop-color="#f7f7f8"/>
      </linearGradient>
      <radialGradient id="toneHat" cx=".45" cy=".55" r=".6">
        <stop offset="0" stop-color="#e9c3a6"/>
        <stop offset=".6" stop-color="#f1e4dc"/>
        <stop offset="1" stop-color="#ffffff"/>
      </radialGradient>
      <radialGradient id="toneCover" cx=".5" cy=".62" r=".6">
        <stop offset="0" stop-color="#e6b796"/>
        <stop offset=".55" stop-color="#d9cbd0"/>
        <stop offset="1" stop-color="#f5efeb"/>
      </radialGradient>
      <linearGradient id="fold" x1="0" x2="1">
        <stop offset="0" stop-color="#000" stop-opacity=".08"/>
        <stop offset="1" stop-color="#000" stop-opacity="0"/>
      </linearGradient>
      <clipPath id="coverPanel"><rect x="780" y="0" width="390" height="880"/></clipPath>
    </defs>

    <rect x="0" y="628" width="300" height="190" fill="url(#toneHat)" role="img" aria-label="Photo of a sleeping baby in a white knitted hat"/>
    <rect x="426" y="79" width="340" height="287" fill="url(#toneCouple)" role="img" aria-label="Photo of a smiling couple in bed, the man wearing a CPAP mask"/>

    <path d="M0,790 C120,830 260,850 414,800 C560,750 680,620 780,552 C900,470 1050,330 1170,200 L1170,880 L0,880 Z" fill="var(--purple)"/>
    <path d="M0,790 C120,830 260,850 414,800 C560,750 680,620 780,552" fill="none" stroke="var(--green)" stroke-width="18"/>

    <g clip-path="url(#coverPanel)">
      <circle cx="963" cy="403" r="232" fill="url(#toneCover)" role="img" aria-label="Photo of a newborn baby sleeping peacefully on a knitted blanket"/>
      <circle cx="963" cy="403" r="232" fill="none" stroke="var(--green)" stroke-width="14"/>
      <path d="M1010,157 A248,248 0 0 1 1211,403" fill="none" stroke="var(--purple)" stroke-width="11"/>
    </g>

    <circle cx="493" cy="738" r="56" fill="var(--seal-gold)" role="img" aria-label="Satisfaction guarantee seal"/>
    <circle cx="670" cy="706" r="54" fill="var(--seal-red)" role="img" aria-label="Free delivery seal"/>

    <rect x="390" y="0" width="14" height="880" fill="url(#fold)"/>
    <rect x="780" y="0" width="14" height="880" fill="url(#fold)"/>
  </svg>

  <!-- Panel 1 -->
  <p class="abs intro">Anyone can give you CPAP supplies. However we are committed to providing you with exceptional customer service too.</p>
  <p class="abs lead">How do we do this? By giving you services no other CPAP retailer offers, like…</p>

  <div class="abs service" style="top:146px">
    <svg class="service-icon" viewBox="0 0 26 26"><rect x="3" y="4" width="20" height="17" rx="2" fill="none" stroke="var(--green)" stroke-width="1.6"/><path d="M3 10h20" stroke="var(--green)" stroke-width="1.6"/></svg>
    <div><div class="service-title">Free Home Visits:</div><div class="service-text">We bring the store to you so we can give you as much time you need &amp; set up all you equipment and supplies for you.</div></div>
  </div>
  <div class="abs service" style="top:238px">
    <svg class="service-icon" viewBox="0 0 26 26"><rect x="2" y="7" width="15" height="11" fill="none" stroke="var(--green)" stroke-width="1.6"/><path d="M17 10h4l3 4v4h-7" fill="none" stroke="var(--green)" stroke-width="1.6"/><circle cx="7" cy="20" r="2" fill="var(--purple)"/><circle cx="20" cy="20" r="2" fill="var(--purple)"/></svg>
    <div><div class="service-title">Free Delivery:</div><div class="service-text">So you never need to come to the store (Unless you want to!).</div></div>
  </div>
  <div class="abs service" style="top:307px">
    <svg class="service-icon" viewBox="0 0 26 26"><path d="M17 5a9 9 0 1 0 4 14a7 7 0 0 1-4-14z" fill="var(--purple)"/><circle cx="6" cy="6" r="1.6" fill="var(--green)"/></svg>
    <div><div class="service-title">Night and Weekend Appointments:</div><div class="service-text">Because not everyone works 9-to-5.</div></div>
  </div>
  <div class="abs service" style="top:360px">
    <svg class="service-icon" viewBox="0 0 26 26"><circle cx="13" cy="13" r="10" fill="none" stroke="var(--purple)" stroke-width="1.6"/><path d="M13 8v10M8 13h10" stroke="var(--purple)" stroke-width="1.6"/></svg>
    <div><div class="service-title">A Dedicated Clinician:</div><div class="service-text">Because we also want to be your friend.</div></div>
  </div>
  <div class="abs service" style="top:413px">
    <svg class="service-icon" viewBox="0 0 26 26"><rect x="3" y="3" width="18" height="18" fill="none" stroke="var(--purple)" stroke-width="1.6" stroke-dasharray="3 2"/><circle cx="17" cy="17" r="5" fill="var(--green)"/></svg>
    <div><div class="service-title">Hardship and Financial-assistance Programs:</div><div class="service-text">To make sure everyone gets the care they need.</div></div>
  </div>
  <div class="abs service" style="top:466px">
    <svg class="service-icon" viewBox="0 0 26 26"><path d="M3 22V15M8 22V11M13 22V8M18 22V13" stroke="var(--purple)" stroke-width="2"/><circle cx="21" cy="5" r="3" fill="var(--green)"/></svg>
    <div><div class="service-title">Promise of Guaranteed Success:</div><div class="service-text">We offer 30-day guarantees on all supplies so you know you are getting the best care possible.</div></div>
  </div>

  <p class="abs settle">Why are YOU Settling for LESS?<br>Let US treat you RIGHT!</p>
  <p class="abs personal">We Make CPAP Personal!</p>

  <!-- Panel 2 -->
  <p class="abs warning">CPAP Doesn’t need to be like this!<span>Let us make sure this doesn’t happen to you</span></p>
  <p class="abs brand-name brand-mid">RestWell Direct</p>

  <div class="abs contact" style="top:458px">
    <svg viewBox="0 0 18 18"><circle cx="9" cy="9" r="9" fill="var(--green)"/><path d="M9 4a3 3 0 0 0-3 3c0 2.5 3 6 3 6s3-3.5 3-6a3 3 0 0 0-3-3z" fill="#fff"/></svg>
    <div>48 Harbour Lane<br>Port Vale, Ontario L0S 1A0<br>Serving all of Ontario</div>
  </div>
  <div class="abs contact" style="top:522px">
    <svg viewBox="0 0 18 18"><circle cx="9" cy="9" r="9" fill="var(--green)"/><path d="M6 5l2 0 1 2.5-1.2 1a6 6 0 0 0 2.7 2.7l1-1.2 2.5 1v2c-4.5 0-8-3.5-8-8z" fill="#fff"/></svg>
    <div>555-014-2290</div>
  </div>
  <div class="abs contact" style="top:549px">
    <svg viewBox="0 0 18 18"><circle cx="9" cy="9" r="9" fill="var(--green)"/><circle cx="9" cy="9" r="5" fill="none" stroke="#fff" stroke-width="1.2"/><path d="M4 9h10M9 4v10" stroke="#fff" stroke-width="1"/></svg>
    <div>www.restwelldirect.example</div>
  </div>

  <p class="abs promise">We Guarantee Your CPAP Success, because your Success is our Reputation.</p>
  <p class="abs tagline-mid">We Bring The Store To You</p>

  <!-- Panel 3 -->
  <p class="abs brand-name brand-cover">RestWell Direct</p>
  <p class="abs cover-head want">WANT SLEEP</p>
  <p class="abs cover-head baby">Like A Baby Again?</p>
  <p class="abs cover-head show">Let us show You How!</p>

  <p class="abs diff">What Makes us Different?</p>
  <ul class="abs perks">
    <li>Everything!</li><li>Free delivery</li>
    <li>Free Home Visits</li><li>Night &amp; weekend appointments</li>
  </ul>
  <p class="abs blurb">We specialize exclusively in Sleep Therapy A dedicated clinician assigned directly to you Hardship and financial-assistance programs</p>
  <p class="abs tagline-cover">We Bring The Store To You</p>
  <div class="abs contact-pill">
    <span><svg width="11" height="11" viewBox="0 0 18 18"><path d="M3 2l4 0 2 4.5-2 1.8a10 10 0 0 0 4.7 4.7l1.8-2 4.5 2v4C9 17 1 9 3 2z" fill="#fff"/></svg>555-014-2290</span>
    <span><svg width="10" height="10" viewBox="0 0 10 10"><circle cx="5" cy="5" r="5" fill="#fff"/></svg>www.restwelldirect.example</span>
  </div>
</div>
</body>
</html>
```